Electrician Company Website Design

I am looking to get a website designed only. I do not need it converted ot html. I simply need the design in a psd format. I have my own team for the conversion. The website is for an electrician company called Bramblecourt electric. I have created a txt document with the project parameters and specifics. I have also uploaded their logo in all avaible formats. It's a zip file.

Number of Pages Required

1 page

```html
<!DOCTYPE html>
<html lang="en">
<head>
<meta charset="UTF-8">
<title>Bramblecourt Electric — Electric Services in Minnesota</title>
<link rel="stylesheet" href="https://fonts.googleapis.com/css2?family=Montserrat:wght@400;500;600;700;800&family=Inter:wght@400;500;600;700&display=swap">
<style>
  :root {
    --ink: #262b45;
    --nav-bg: #232323;
    --page-bg: #f2f6fa;
    --white: #ffffff;
    --brand-blue: #0e63ad;
    --deep-blue: #12497e;
    --slate-blue: #2d5380;
    --brick-red: #922b2b;
    --amber: #cf9a2f;
    --map-blue: #9ec0df;
    --footer-bg: #232323;
    --field-border: #cfd4da;
    --field-bg: #f6f7f9;
  }
  * { box-sizing: border-box; margin: 0; padding: 0; }
  html, body { width: 1200px; height: 3872px; overflow: hidden; }
  body {
    position: relative;
    background: var(--page-bg);
    font-family: "Montserrat", sans-serif;
    color: var(--ink);
  }
  .abs { position: absolute; }

  /* Navigation */
  .site-nav { left: 0; top: 0; width: 1200px; height: 83px; background: var(--nav-bg); }
  .brand { left: 168px; top: 29px; color: var(--white); font-weight: 700; font-size: 18px; display: flex; align-items: center; gap: 8px; }
  .brand-dot { width: 14px; height: 14px; border-radius: 50%; background: var(--brand-blue); }
  .nav-link { top: 29px; font-family: "Inter", sans-serif; font-weight: 700; font-size: 19px; color: var(--white); }
  .nav-active { left: 601px; top: 58px; width: 55px; height: 5px; background: var(--brand-blue); }

  /* Hero */
  .hero { left: 0; top: 83px; width: 1200px; height: 484px;
    background:
      linear-gradient(90deg, rgba(225,231,238,0.55) 0%, rgba(225,231,238,0.72) 30%, rgba(225,231,238,0.45) 60%, rgba(225,231,238,0.15) 100%),
      radial-gradient(ellipse 320px 380px at 90px 140px, #8b7a66 0%, rgba(139,122,102,0) 100%),
      radial-gradient(ellipse 260px 200px at 1130px 330px, #c9c56a 0%, rgba(201,197,106,0) 100%),
      radial-gradient(ellipse 420px 300px at 640px 300px, #5f8fc4 0%, rgba(95,143,196,0) 100%),
      linear-gradient(100deg, #5a5c63 0%, #7b8796 30%, #6d8fb6 55%, #8aa0b8 80%, #8e9a8a 100%); }
  .hero-title { left: 203px; top: 188px; font-weight: 800; font-size: 35px; line-height: 41px; color: var(--ink); letter-spacing: 0.5px; }
  .hero-text { left: 203px; top: 275px; width: 410px; font-size: 15.5px; line-height: 20px; font-weight: 500; color: #1c1f2c; }
  .btn { background: var(--brand-blue); color: var(--white); font-weight: 600; display: flex; align-items: center; justify-content: center; border-radius: 2px; }
  .hero-btn { left: 203px; top: 388px; width: 122px; height: 45px; font-size: 19px; }
  .hero-map { left: 812px; top: 165px; width: 293px; height: 313px; border-radius: 22px;
    background: radial-gradient(ellipse 120px 90px at 140px 150px, #6f89a6 0%, #9ec0df 70%), var(--map-blue); }

  /* Info strip */
  .info-cell { top: 508px; width: 302px; height: 116px; color: var(--white); }
  .info-cell h3 { position: absolute; left: 72px; top: 17px; font-size: 16px; font-weight: 700; }
  .info-cell p { position: absolute; left: 72px; top: 40px; width: 215px; font-size: 12.5px; line-height: 15.5px; font-weight: 500; }
  .info-cell svg { position: absolute; left: 16px; top: 20px; }
  .info-services { left: 143px; background: var(--slate-blue); }
  .info-area { left: 445px; background: var(--brick-red); }
  .info-contact { left: 745px; width: 302px; background: var(--amber); }

  /* About */
  .about-img { left: 48px; top: 720px; width: 460px; height: 316px;
    background:
      radial-gradient(ellipse 170px 120px at 230px 150px, rgba(20,20,24,0.75) 0%, rgba(20,20,24,0) 100%),
      linear-gradient(180deg, #b32a2a 0%, #a82727 58%, #262626 58%, #1f1f1f 100%);
    border-bottom: 3px solid #b32a2a; }
  .about-title { left: 576px; top: 787px; font-size: 30px; font-weight: 800; color: var(--ink); }
  .about-text { left: 576px; top: 842px; width: 500px; font-size: 15px; line-height: 18.5px; font-weight: 500; color: #1c1f2c; }
  .about-btn { left: 571px; top: 946px; width: 160px; height: 47px; font-size: 18px; }

  /* Services */
  .services { left: 0; top: 1178px; width: 1200px; height: 555px; background: var(--white); }
  .section-title { width: 1200px; left: 0; text-align: center; font-size: 36px; font-weight: 700; color: var(--ink); }
  .section-text { left: 0; width: 1200px; text-align: center; font-weight: 500; color: #1c1f2c; }
  .service-card { top: 1378px; width: 254px; height: 255px; background: var(--page-bg); }
  .service-card .photo { position: absolute; left: 0; top: 0; width: 254px; height: 134px; }
  .service-card h4 { position: absolute; left: 0; top: 148px; width: 254px; text-align: center; font-size: 15px; line-height: 18px; font-weight: 700; color: #1c1f2c; }
  .service-card .btn { position: absolute; left: 77px; top: 204px; width: 100px; height: 28px; font-size: 11px; }

  /* Gallery */
  .gallery-photo { top: 1970px; height: 319px; }
  .chevron { top: 2108px; }

  /* Call to action */
  .cta { left: 0; top: 2399px; width: 1200px; height: 674px; background: var(--deep-blue); }
  .cta-title { left: 162px; top: 2515px; font-size: 34px; line-height: 48px; font-weight: 700; color: var(--white); }
  .cta-text { left: 162px; top: 2626px; width: 370px; font-size: 11.5px; line-height: 16px; color: var(--white); }
  .cta-map { left: 732px; top: 2485px; width: 216px; height: 245px; border-radius: 18px;
    background: linear-gradient(160deg, #a7c7e4 0%, #94b7d8 100%); }

  /* Quote form */
  .quote-photo { left: 171px; top: 2812px; width: 285px; height: 577px;
    background:
      radial-gradient(ellipse 110px 150px at 140px 190px, #c9a48c 0%, rgba(201,164,140,0) 100%),
      radial-gradient(ellipse 160px 220px at 150px 430px, #eef0f2 0%, rgba(238,240,242,0) 100%),
      linear-gradient(160deg, #2d3138 0%, #4e545c 40%, #b8bcc2 75%, #dcdde0 100%); }
  .quote-card { left: 456px; top: 2812px; width: 573px; height: 548px; background: var(--white); }
  .quote-title { left: 498px; top: 2852px; font-size: 32px; font-weight: 700; color: var(--ink); }
  .field-label { left: 498px; font-size: 11.5px; font-weight: 600; color: #333; }
  .field { left: 498px; width: 489px; height: 40px; border: 1px solid var(--field-border); background: var(--field-bg); border-radius: 3px;
    font-size: 11.5px; color: #666; display: flex; align-items: center; padding-left: 18px; }
  .field svg { position: absolute; right: 16px; top: 15px; }
  .quote-btn { left: 498px; top: 3270px; width: 489px; height: 37px; font-size: 11.5px; font-weight: 700; border-radius: 3px; }

  /* Footer */
  .footer { left: 0; top: 3422px; width: 1200px; height: 450px; background: var(--footer-bg); }
  .footer-title { left: 0; width: 1182px; top: 3530px; text-align: center; font-family: "Inter", sans-serif; font-size: 36px; font-weight: 700; color: var(--white); }
  .footer-h { top: 3612px; font-family: "Inter", sans-serif; font-size: 20px; font-weight: 700; color: var(--white); }
  .footer-p { font-family: "Inter", sans-serif; font-size: 16.5px; line-height: 20px; color: var(--white); }
  .social { top: 3720px; width: 40px; height: 40px; border-radius: 50%; background: var(--brand-blue); }
  .sub-input { left: 611px; top: 3716px; width: 263px; height: 36px; background: #e9e9e9; font-family: "Inter", sans-serif; font-size: 12.5px; color: #666; display: flex; align-items: center; padding-left: 13px; }
  .sub-btn { left: 874px; top: 3716px; width: 114px; height: 36px; font-family: "Inter", sans-serif; font-size: 15px; font-weight: 700; border-radius: 0; }
</style>
</head>
<body>

<!-- Navigation -->
<header class="site-nav abs"></header>
<div class="brand abs"><span class="brand-dot"></span>Bramblecourt Electric</div>
<nav>
  <span class="nav-link abs" style="left:601px">Home</span>
  <span class="nav-link abs" style="left:683px">Services</span>
  <span class="nav-link abs" style="left:785px">Contact</span>
  <span class="nav-link abs" style="left:880px">Gallery</span>
  <span class="nav-link abs" style="left:969px">FAQs</span>
</nav>
<div class="nav-active abs"></div>

<!-- Hero -->
<section class="hero abs" role="img" aria-label="Electrician working on blue wiring in a distribution panel"></section>
<h1 class="hero-title abs">ELECTRIC SERVICES<br>COMPANY IN MINNESOTA</h1>
<p class="hero-text abs">Bramblecourt Electric has been providing quality electrical services to Minnesota residents for over 20 years. We take pride in our customer service and quality workmanship.</p>
<div class="btn hero-btn abs">CONTACT</div>
<div class="hero-map abs" role="img" aria-label="Map of Minnesota with company emblem"></div>

<!-- Info strip -->
<div class="info-cell info-services abs">
  <svg width="36" height="48" viewBox="0 0 36 48"><rect x="0" y="0" width="36" height="14" fill="#fff"/><rect x="0" y="17" width="36" height="14" fill="#fff"/><rect x="0" y="34" width="36" height="14" fill="#fff"/></svg>
  <h3>OUR SERVICES</h3>
  <p>Residential Electrical Services, Commerical Electrical Services, Industrial Electrical Services.</p>
</div>
<div class="info-cell info-area abs">
  <svg width="36" height="48" viewBox="0 0 36 48"><path d="M18 0C8 0 0 8 0 18c0 13 18 30 18 30s18-17 18-30C36 8 28 0 18 0z" fill="#fff"/><circle cx="18" cy="18" r="7" fill="#922b2b"/></svg>
  <h3>SERVICE AREA</h3>
  <p>We offer our services in central Minnesota and the surrounding counties.</p>
</div>
<div class="info-cell info-contact abs">
  <svg width="44" height="44" viewBox="0 0 24 24"><path d="M6.6 10.8c1.4 2.8 3.8 5.1 6.6 6.6l2.2-2.2c.3-.3.7-.4 1-.2 1.1.4 2.3.6 3.6.6.6 0 1 .4 1 1V20c0 .6-.4 1-1 1C10.6 21 3 13.4 3 4c0-.6.4-1 1-1h3.5c.6 0 1 .4 1 1 0 1.3.2 2.5.6 3.6.1.3 0 .7-.2 1L6.6 10.8z" fill="#fff"/></svg>
  <h3>CONTACT</h3>
  <p>Phone: 555 014 2290<br>1150 Larkfield Ave NE<br>Alder Falls, MN 55099</p>
</div>

<!-- About -->
<div class="about-img abs" role="img" aria-label="Company emblem on a red and black background"></div>
<h2 class="about-title abs">BRAMBLECOURT ELECTRIC</h2>
<p class="about-text abs">Lorem ipsum dolor sit amet, consectetur adipiscing elit, sed do eiusmod tempor incididunt ut labore et dolore magna aliqua. Lorem ipsum dolor sit amet, consectetur adipiscing elit, sed do eiusmod tempor incididunt ut labore et dolore magna aliqua.</p>
<div class="btn about-btn abs">LEARN MORE</div>

<!-- Services -->
<section class="services abs"></section>
<h2 class="section-title abs" style="top:1226px">SERVICES</h2>
<p class="section-text abs" style="top:1283px;font-size:15px;line-height:18px">Lorem ipsum dolor sit amet, consectetur adipiscing elit, sed do<br>eiusmod tempor incididunt ut labore et dolore magna aliqua.</p>

<article class="service-card abs" style="left:193px">
  <div class="photo" role="img" aria-label="Electrician inspecting a commercial panel" style="background:radial-gradient(ellipse 70px 60px at 60px 60px,#9a7f68 0%,rgba(154,127,104,0) 100%),radial-gradient(ellipse 80px 70px at 190px 70px,#6f9cc9 0%,rgba(111,156,201,0) 100%),linear-gradient(135deg,#2f3a48,#54657a 55%,#8a98a6)"></div>
  <h4>Commerical Electrical<br>Services</h4>
  <div class="btn">LEARN MORE</div>
</article>
<article class="service-card abs" style="left:463px">
  <div class="photo" role="img" aria-label="Electrician installing a ceiling fixture at home" style="background:radial-gradient(ellipse 40px 60px at 105px 75px,#8a7a70 0%,rgba(138,122,112,0) 100%),linear-gradient(90deg,#dcdcdc,#ececec 60%,#f6f6f6 75%,#e2e2e2)"></div>
  <h4>Residential Electrical<br>Services</h4>
  <div class="btn">LEARN MORE</div>
</article>
<article class="service-card abs" style="left:734px">
  <div class="photo" role="img" aria-label="Engineer checking a rooftop solar array" style="background:radial-gradient(ellipse 40px 70px at 195px 70px,#2c4f8e 0%,rgba(44,79,142,0) 100%),linear-gradient(180deg,#c7d9ec,#a9c3df 45%,#4b6585 62%,#2c3b52 85%,#6a6f78)"></div>
  <h4>Industrial Electrical<br>Services</h4>
  <div class="btn">LEARN MORE</div>
</article>

<!-- Gallery -->
<h2 class="section-title abs" style="top:1814px">PROJECTS GALLERY</h2>
<p class="section-text abs" style="top:1878px;font-size:18px;line-height:22px">Lorem ipsum dolor sit amet, consectetur adipiscing elit, sed do<br>eiusmod tempor incididunt ut labore et dolore magna.</p>
<div class="gallery-photo abs" role="img" aria-label="Industrial grain facility project" style="left:0;width:354px;background:radial-gradient(ellipse 160px 80px at 120px 40px,#e6ebf0 0%,rgba(230,235,240,0) 100%),linear-gradient(180deg,#6f8fb4 0%,#a9b9c9 30%,#b8bcbf 50%,#8a8f94 70%,#5a5e62 90%,#eceff1 100%)"></div>
<div class="gallery-photo abs" role="img" aria-label="Residential townhouse project" style="left:365px;width:468px;background:radial-gradient(ellipse 130px 70px at 90px 250px,#3f6b2c 0%,rgba(63,107,44,0) 100%),radial-gradient(ellipse 110px 90px at 400px 240px,#6c8a3a 0%,rgba(108,138,58,0) 100%),linear-gradient(180deg,#3a4a50 0%,#34444a 55%,#2e3b30 75%,#3c5a2c 100%)"></div>
<div class="gallery-photo abs" role="img" aria-label="Modern apartment building project" style="left:844px;width:356px;background:radial-gradient(ellipse 70px 120px at 40px 200px,#2d4a2c 0%,rgba(45,74,44,0) 100%),linear-gradient(180deg,#d3d7db 0%,#b7bcc1 35%,#7f868d 60%,#4a4f56 82%,#3a3e44 100%)"></div>
<svg class="chevron abs" style="left:112px" width="26" height="36" viewBox="0 0 26 36"><path d="M20 3L6 18l14 15" fill="none" stroke="#fff" stroke-width="3"/></svg>
<svg class="chevron abs" style="left:1048px" width="26" height="36" viewBox="0 0 26 36"><path d="M6 3l14 15L6 33" fill="none" stroke="#fff" stroke-width="3"/></svg>

<!-- Call to action -->
<section class="cta abs"></section>
<h2 class="cta-title abs">Need Electrical services?<br>We’re here to help!</h2>
<p class="cta-text abs">The gradual accumulation of information about atomic and small-scale behaviour during the first quarter of the 20th</p>
<div class="cta-map abs" role="img" aria-label="Map of Minnesota"></div>

<!-- Quote form -->
<div class="quote-photo abs" role="img" aria-label="Customer support agent wearing a headset"></div>
<section class="quote-card abs"></section>
<h2 class="quote-title abs">Get A Free Quote Here</h2>
<label class="field-label abs" style="top:2930px">Name*</label>
<div class="field abs" style="top:2957px">Full Name</div>
<label class="field-label abs" style="top:3010px">Email*</label>
<div class="field abs" style="top:3037px">example@gmail.com</div>
<label class="field-label abs" style="top:3091px">Service Type *</label>
<div class="field abs" style="top:3118px">Please Select<svg width="12" height="8" viewBox="0 0 12 8"><path d="M1 1l5 5 5-5" fill="none" stroke="#555" stroke-width="1.6"/></svg></div>
<label class="field-label abs" style="top:3167px">Time *</label>
<div class="field abs" style="top:3194px">4:00 Available<svg width="12" height="8" viewBox="0 0 12 8"><path d="M1 1l5 5 5-5" fill="none" stroke="#555" stroke-width="1.6"/></svg></div>
<div class="btn quote-btn abs">BOOK APPOINTMENT</div>

<!-- Footer -->
<footer class="footer abs"></footer>
<h2 class="footer-title abs">GET IN TOUCH</h2>
<h3 class="footer-h abs" style="left:214px">CONTACT US</h3>
<p class="footer-p abs" style="left:214px;top:3650px">Email us: hello@bramblecourtelectric.com</p>
<p class="footer-p abs" style="left:214px;top:3680px">Phone: +555 014 2290</p>
<span class="social abs" style="left:218px" role="img" aria-label="Social profile"></span>
<span class="social abs" style="left:266px" role="img" aria-label="Social profile"></span>
<span class="social abs" style="left:314px" role="img" aria-label="Social profile"></span>
<h3 class="footer-h abs" style="left:611px">SUBSCRIBE</h3>
<p class="footer-p abs" style="left:611px;top:3650px;width:345px">Get special offers and exclusive discounts when you subscribe to our newsletter.</p>
<div class="sub-input abs">Your best email</div>
<div class="btn sub-btn abs">SUBSCRIBE</div>

</body>
</html>
```